Design graphics and Print for a line of Herb Seeds- Envelope Design

We need a set of herb seed envelopes designed for a new seed line we are launching.
The design will be both front and back

Envelope will be a colored ( green) ) envelope with white text
or a white or cream envelope in all black /and images text. Or can add some colors to the white envelope.

I have attached the die-cut of the seed envelope.
I have attached some images of envelopes I like. Please do not copy, these are just to give you an idea of what I like.

Please feel free to reach out to me if you have any questions.

Thank you

Target Market(s)

The design needs to classic that can translate to 3 different audiences. 1. young parents 2. hip, young single millennial 3. kids

Industry/Entity Type

Ecommerce

Font styles to use
Serif

Requirements
Must have
• Please use the herb - Parsley for the design
Icon, Text or both.

Front side must have:
1.either herb Icon or work Parsley or both- this will be the main attraction
2. company name- Tin Lantern Sundries
3. can use design elements
4. can use my logo on from or back or not at all. I

Backside must have:
1. social media tags
FB, Instagram and Pinterest ( use icons) @tinlanternsundries

my website: www.tinlanternsundries.example
this can be on from or back of the envelope.
Should not have
• please stay away from "county" flowery, old fashioned style designs

```html
<!DOCTYPE html>
<html lang="en">
<head>
<meta charset="utf-8">
<title>Tin Lantern Sundries – Parsley Seed Envelope</title>
<link rel="stylesheet" href="https://fonts.googleapis.com/css2?family=Cormorant+Garamond:wght@300;400;500&display=swap">
<style>
  :root {
    --backdrop: #161616;
    --envelope: #27382f;
    --envelope-fold: #22322a;
    --seam: rgba(255, 255, 255, 0.07);
    --ink: #e6e8e3;
    --ink-soft: #c9cfc8;
    --accent: #3f7a62;
    --leaf-light: #b9c2b6;
    --leaf-dark: #55665b;
  }
  * { box-sizing: border-box; margin: 0; padding: 0; }
  html, body { width: 1200px; height: 900px; overflow: hidden; }
  body {
    background: var(--backdrop);
    font-family: "Cormorant Garamond", Georgia, serif;
    color: var(--ink);
    position: relative;
  }
  .envelope {
    position: absolute;
    top: 190px;
    width: 350px;
    height: 520px;
    background: var(--envelope);
    overflow: hidden;
  }
  .envelope--back { left: 215px; }
  .envelope--front { left: 635px; }

  .envelope__seams { position: absolute; inset: 0; }

  .back-copy {
    position: absolute;
    top: 70px;
    left: 40px;
    right: 40px;
    text-align: center;
    font-weight: 400;
  }
  .back-copy__brand { font-size: 17px; letter-spacing: 0.3px; }
  .back-copy__herb { font-size: 21px; letter-spacing: 1.5px; margin: 4px 0 6px; }
  .back-copy__text { font-size: 14.5px; line-height: 1.3; color: var(--ink-soft); }

  .socials {
    list-style: none;
    margin: 22px 0 0;
    text-align: left;
    padding-left: 20px;
  }
  .socials__item {
    display: flex;
    align-items: center;
    gap: 7px;
    font-size: 14px;
    line-height: 1.45;
  }
  .socials__dot {
    width: 11px; height: 11px;
    border-radius: 50%;
    background: var(--ink);
    flex: none;
  }
  .back-copy__web { font-size: 14.5px; margin-top: 6px; text-align: left; padding-left: 20px; }

  .herb-illustration {
    position: absolute;
    left: 90px;
    top: 155px;
    width: 230px;
    height: 250px;
    border-radius: 48% 52% 40% 45%;
    background: radial-gradient(ellipse at 50% 40%, var(--leaf-light) 0%, var(--leaf-dark) 55%, rgba(39, 56, 47, 0) 78%);
    opacity: 0.55;
  }
  .herb-word {
    position: absolute;
    left: 28px;
    top: 318px;
    font-size: 76px;
    font-weight: 300;
    letter-spacing: 4px;
    color: var(--ink);
    line-height: 1;
  }
  .brand-mark {
    position: absolute;
    right: 26px;
    top: 52px;
    display: flex;
    align-items: center;
    gap: 8px;
    font-size: 14px;
    font-weight: 400;
    color: var(--accent);
  }
  .brand-mark__circle {
    width: 30px; height: 30px;
    border-radius: 50%;
    border: 1.5px solid var(--accent);
  }
</style>
</head>
<body>

  <section class="envelope envelope--back" aria-label="Envelope back">
    <svg class="envelope__seams" width="350" height="520" viewBox="0 0 350 520" aria-hidden="true">
      <path d="M40 0 V60 Q40 72 52 72 H298 Q310 72 310 60 V0" fill="none" stroke="var(--seam)" stroke-width="2"/>
      <path d="M0 330 L120 430 Q130 440 140 440 H210 Q220 440 230 430 L350 330" fill="none" stroke="var(--seam)" stroke-width="2"/>
      <path d="M310 72 V330" fill="none" stroke="var(--seam)" stroke-width="1.5"/>
    </svg>
    <div class="back-copy">
      <p class="back-copy__brand">Tin Lantern Sundries</p>
      <h2 class="back-copy__herb">PARSLEY</h2>
      <p class="back-copy__text">Lorem ipsum dolor sit amet, consectetuer adipiscing elit, sed diam nonummy nibh euismod tincidunt ut laoreet dolore magna aliquam erat volutpat. Ut wisi enim ad minim veniam, quis nostrud</p>
      <ul class="socials">
        <li class="socials__item"><span class="socials__dot"></span>@tinlanternsundries</li>
        <li class="socials__item"><span class="socials__dot"></span>@tinlanternsundries</li>
        <li class="socials__item"><span class="socials__dot"></span>@tinlanternsundries</li>
      </ul>
      <p class="back-copy__web">www.tinlanternsundries.example</p>
    </div>
  </section>

  <section class="envelope envelope--front" aria-label="Envelope front">
    <div class="brand-mark">
      <span class="brand-mark__circle"></span>
      <span>Tin Lantern Sundries</span>
    </div>
    <div class="herb-illustration" role="img" aria-label="Fine line drawing of a parsley sprig with three leafy branches"></div>
    <h1 class="herb-word">parsley</h1>
  </section>

</body>
</html>
```